Catering company looking to promote business

We need a flyer design for our company named "Peel and Pulp." We cater/deliver açaí bowls and smoothies.

The objective of this flyer is to let companies know that we are taking açaí bowls and smoothie orders and they can be delivered to them.

Some key points we would like on the flyer:
- Photo of açaí bowl and smoothie
- Menu w/ pricing
- "No hidden delivery fees"
- 5 bowl or smoothie minimum
- Online ordering through website:
https://tillbox.example/shop/peelandpulp
- For the month of February --> Get one free topping and drizzle!
- FRIDAY DELIVERIES ONLY
- Questions? Call (555) 730-9182
- social media friendwall & snapreel @pnpulp
- website www.peelandpulp.example

font - hello beautiful

Target Market(s)

Juice, smoothies, açaí bowls

Industry/Entity Type

Business

Font styles to use
Other font styles liked:
• Hello Beautiful

Colors
a64599
b768aa
d3a5cc
eedced
f7f1f7
9bcb3c

Requirements
Must have
• Please match logo, fonts, color schemes, etc.

```html
<!DOCTYPE html>
<html lang="en">
<head>
<meta charset="utf-8">
<title>Peel and Pulp – Açaí Bowl Delivery Flyer</title>
<link rel="stylesheet" href="https://fonts.googleapis.com/css2?family=Amatic+SC:wght@400;700&family=Lato:wght@400;700&family=Great+Vibes&display=swap">
<style>
  :root {
    --plum: #a64599;
    --orchid: #b768aa;
    --lilac: #d3a5cc;
    --blush: #eedced;
    --mist: #f7f1f7;
    --leaf: #9bcb3c;
    --leaf-deep: #5fa02a;
    --ink: #3a3a3a;
    --backdrop: #6b6b6b;
  }
  * { box-sizing: border-box; margin: 0; padding: 0; }
  html, body { width: 1200px; height: 1200px; overflow: hidden; }
  body { background: var(--backdrop); position: relative; font-family: "Lato", sans-serif; }

  .flyer {
    position: absolute; left: 193px; top: 30px;
    width: 814px; height: 1140px;
    background: #fff; overflow: hidden;
  }
  .photo { position: absolute; }
  .photo-bananas {
    left: 0; top: 0; width: 302px; height: 198px;
    background: radial-gradient(ellipse at 45% 45%, #f3ead0 0%, #e8dcb4 45%, rgba(255,255,255,0) 75%);
  }
  .photo-bowl {
    left: 386px; top: -40px; width: 470px; height: 433px;
    border-radius: 50%;
    background: radial-gradient(circle at 40% 50%, #f1e8d6 0%, #d8c9b0 25%, #3a3d6a 38%, #d8343c 58%, #b51f2c 75%, #5d4a8a 92%);
  }
  .photo-berries {
    left: 312px; top: 272px; width: 148px; height: 84px;
    border-radius: 40%;
    background: radial-gradient(ellipse at 50% 55%, #2a2a34 0%, #3b3b48 45%, #6aa53a 70%, rgba(255,255,255,0) 78%);
  }
  .photo-cup {
    left: 293px; top: 854px; width: 195px; height: 167px;
    border-radius: 20px 20px 60px 60px;
    background: linear-gradient(180deg, #d9433f 0%, #c2394a 35%, #e6d6b8 50%, #6e2b4a 70%, #4f1f3a 100%);
  }
  .photo-strawberries {
    left: 692px; top: 985px; width: 122px; height: 132px;
    border-radius: 45%;
    background: radial-gradient(ellipse at 50% 50%, #e0353a 0%, #c9242b 50%, rgba(255,255,255,0) 72%);
  }

  .title {
    position: absolute; left: 33px; top: 248px;
    font-family: "Amatic SC", cursive; font-weight: 700;
    font-size: 86px; color: var(--plum); line-height: 1;
  }
  .price {
    position: absolute; left: 102px; top: 342px;
    font-family: "Amatic SC", cursive; font-weight: 700;
    font-size: 72px; color: var(--leaf-deep); line-height: 1;
  }
  .description {
    position: absolute; left: 44px; top: 432px; width: 740px;
    font-family: "Amatic SC", cursive; font-weight: 700;
    font-size: 33px; color: var(--orchid); line-height: 1.15;
    text-transform: uppercase;
  }

  .extras {
    position: absolute; left: 49px; top: 538px; width: 723px; height: 152px;
    border: 3px solid var(--plum);
    background: linear-gradient(180deg, #fff 0%, #f4f4f4 100%);
  }
  .extras-legend {
    position: absolute; left: 50%; top: -24px; transform: translateX(-50%);
    background: #fff; padding: 0 14px; white-space: nowrap;
    font-family: "Amatic SC", cursive; font-weight: 700;
    font-size: 36px; color: var(--leaf-deep); line-height: 1.2;
    text-transform: uppercase;
  }
  .col { position: absolute; top: 34px; }
  .col-heading {
    font-family: "Amatic SC", cursive; font-weight: 700;
    font-size: 20px; color: var(--plum); text-transform: uppercase; line-height: 1;
  }
  .col-price {
    font-family: "Amatic SC", cursive; font-weight: 700;
    font-size: 18px; color: var(--leaf-deep); line-height: 1.2;
  }
  .col ul, .col-list ul { list-style: none; font-size: 16px; color: var(--ink); line-height: 1.25; }
  .col ul { margin-top: 2px; }
  .col-list { position: absolute; top: 78px; }
  .divider { position: absolute; width: 1px; background: #555; }

  .fees {
    position: absolute; left: 32px; top: 714px;
    font-family: "Amatic SC", cursive; font-weight: 700;
    font-size: 56px; color: var(--leaf-deep); line-height: 1;
    text-shadow: -2px 0 0 var(--orchid);
    text-transform: uppercase;
  }
  .minimum { position: absolute; left: 50px; top: 776px; display: flex; align-items: baseline; gap: 16px; }
  .minimum-count {
    font-family: "Amatic SC", cursive; font-weight: 700;
    font-size: 60px; color: var(--plum); line-height: 1; text-transform: uppercase;
  }
  .minimum-note { font-size: 24px; color: var(--ink); }

  .promo {
    position: absolute; left: 474px; top: 745px; width: 307px; height: 276px;
    background: var(--blush);
  }
  .promo-label {
    position: absolute; left: 24px; top: 20px;
    font-family: "Great Vibes", cursive; font-size: 25px; color: var(--plum);
  }
  .promo-url {
    position: absolute; left: 24px; top: 55px; width: 262px;
    font-size: 13.5px; color: var(--ink);
    border-bottom: 1px solid var(--ink); padding-bottom: 3px;
  }
  .promo-month-lead {
    position: absolute; left: 28px; top: 86px;
    font-family: "Great Vibes", cursive; font-size: 13px; color: var(--plum);
  }
  .promo-month {
    position: absolute; left: 40px; top: 106px;
    font-family: "Great Vibes", cursive; font-size: 38px; color: var(--leaf-deep); line-height: 1;
  }
  .promo-split { position: absolute; left: 156px; top: 94px; width: 1px; height: 52px; background: var(--plum); }
  .promo-offer-lead {
    position: absolute; left: 164px; top: 100px;
    font-family: "Great Vibes", cursive; font-size: 14px; color: var(--plum);
  }
  .promo-offer {
    position: absolute; left: 164px; top: 118px; white-space: nowrap;
    font-family: "Amatic SC", cursive; font-weight: 700;
    font-size: 17px; color: var(--plum); text-transform: uppercase;
  }
  .promo-delivery { position: absolute; left: 48px; top: 168px; display: flex; align-items: flex-end; gap: 12px; }
  .promo-day {
    font-family: "Amatic SC", cursive; font-weight: 700;
    font-size: 38px; color: var(--plum); line-height: 1; text-transform: uppercase;
  }
  .promo-day-note {
    font-family: "Amatic SC", cursive; font-weight: 700;
    font-size: 19px; color: var(--plum); text-transform: uppercase; margin-left: -6px;
  }

  .brand {
    position: absolute; left: 23px; top: 930px; width: 186px; height: 186px;
    border-radius: 50%; border: 5px solid var(--orchid);
    background: #fff;
    display: flex; align-items: center; justify-content: center; text-align: center;
  }
  .brand-name {
    font-family: "Amatic SC", cursive; font-weight: 700;
    font-size: 44px; line-height: 0.95; color: var(--plum);
  }

  .contact-band {
    position: absolute; left: 205px; top: 1047px; width: 609px; height: 70px;
    background: var(--orchid); color: #fff;
  }
  .contact-label {
    position: absolute; left: 14px; top: 6px;
    font-family: "Amatic SC", cursive; font-weight: 700; font-size: 18px; text-transform: uppercase;
  }
  .contact-row {
    position: absolute; left: 14px; top: 36px; display: flex; gap: 14px; white-space: nowrap;
    font-size: 17px; font-weight: 700;
  }
  .contact-icon { position: absolute; top: 12px; }
</style>
</head>
<body>
  <main class="flyer">
    <div class="photo photo-bananas" role="img" aria-label="Photo of sliced bananas"></div>
    <div class="photo photo-bowl" role="img" aria-label="Photo of açaí bowl topped with bananas, blueberries, strawberries and coconut"></div>
    <div class="photo photo-berries" role="img" aria-label="Photo of açaí berries with leaves"></div>

    <h1 class="title">açaí bowl</h1>
    <p class="price">$9.00</p>
    <p class="description">Açaí sorbet topped with granola, bananas, strawberries, blueberries, coconut shavings and drizzled with honey</p>

    <section class="extras">
      <h2 class="extras-legend">Want to add something extra?</h2>

      <div class="col" style="left:37px;">
        <h3 class="col-heading">Fruits</h3>
        <p class="col-price">$1.00</p>
        <ul><li>Bananas</li><li>Strawberries</li><li>Blueberries</li></ul>
      </div>

      <div class="col" style="left:215px;">
        <h3 class="col-heading">Toppings</h3>
        <p class="col-price">.50¢</p>
        <ul><li>Almonds</li><li>Chia seeds</li><li>Hemp seeds</li></ul>
      </div>
      <div class="divider" style="left:318px; top:84px; height:52px;"></div>
      <div class="col-list" style="left:330px;">
        <ul><li>Quinoa puffs</li><li>Coconut shavings</li><li>Granola</li></ul>
      </div>

      <div class="col" style="left:532px;">
        <h3 class="col-heading">Drizzle</h3>
        <p class="col-price">.50¢</p>
        <ul><li>Peanut butter</li><li>Almond butter</li><li>Honey</li></ul>
      </div>
      <div class="divider" style="left:645px; top:84px; height:44px;"></div>
      <div class="col-list" style="left:658px;">
        <ul><li>Agave</li></ul>
      </div>
    </section>

    <p class="fees">"No hidden delivery fees"</p>
    <p class="minimum"><span class="minimum-count">5 bowl</span><span class="minimum-note">or smoothie minimum</span></p>

    <aside class="promo">
      <p class="promo-label">Online ordering through website</p>
      <p class="promo-url">https://tillbox.example/shop/peelandpulp</p>
      <p class="promo-month-lead">For the month of</p>
      <p class="promo-month">February</p>
      <div class="promo-split"></div>
      <p class="promo-offer-lead">Get one</p>
      <p class="promo-offer">Free topping and drizzle</p>
      <div class="promo-delivery">
        <svg width="50" height="40" viewBox="0 0 50 40" aria-hidden="true">
          <rect x="2" y="4" width="28" height="22" fill="var(--plum)"/>
          <path d="M32 10 h9 l7 9 v7 h-16 z" fill="var(--plum)"/>
          <circle cx="12" cy="31" r="6" fill="var(--plum)" stroke="var(--blush)" stroke-width="2"/>
          <circle cx="38" cy="31" r="6" fill="var(--plum)" stroke="var(--blush)" stroke-width="2"/>
        </svg>
        <span class="promo-day">Friday</span>
        <span class="promo-day-note">deliveries only</span>
      </div>
    </aside>

    <div class="photo photo-cup" role="img" aria-label="Photo of açaí bowl in a takeaway cup"></div>

    <div class="brand"><span class="brand-name">Peel and<br>Pulp</span></div>

    <footer class="contact-band">
      <p class="contact-label">Questions? Call</p>
      <svg class="contact-icon" style="left:236px;" width="20" height="20" viewBox="0 0 20 20" aria-hidden="true">
        <circle cx="10" cy="10" r="8" fill="none" stroke="#fff" stroke-width="1.6"/>
        <ellipse cx="10" cy="10" rx="3.5" ry="8" fill="none" stroke="#fff" stroke-width="1.4"/>
        <line x1="2" y1="10" x2="18" y2="10" stroke="#fff" stroke-width="1.4"/>
      </svg>
      <svg class="contact-icon" style="left:392px; top:15px;" width="12" height="12" viewBox="0 0 12 12" aria-hidden="true">
        <circle cx="6" cy="6" r="5" fill="#fff"/>
      </svg>
      <div class="contact-row">
        <span>(555) 730-9182</span>
        <span>www.peelandpulp.example</span>
        <span>@pnpulp</span>
      </div>
    </footer>

    <div class="photo photo-strawberries" role="img" aria-label="Photo of fresh strawberries"></div>
  </main>
</body>
</html>
```